Business Card Design Project OakVRT

Business card that looks professional but stands out!

Industry/Entity Type

Business

Requirements
Must have
• Tailor to Realtors
loan products on the back of the card

```html
<!DOCTYPE html>
<html lang="en">
<head>
<meta charset="utf-8">
<title>OakVRT Mortgage – Business Card</title>
<link href="https://fonts.googleapis.com/css2?family=Arimo:wght@400;700&display=swap" rel="stylesheet">
<style>
  :root {
    --backdrop: #2b2b2b;
    --card-white: #ffffff;
    --brand-blue: #0a4f9c;
    --band-grey: #9a9a9a;
    --panel-grey-light: #b4b4b4;
    --panel-grey-dark: #8e8e8e;
    --text-grey: #7a7a7a;
    --text-white: #ffffff;
  }
  * { box-sizing: border-box; margin: 0; padding: 0; }
  html, body { width: 1200px; height: 900px; overflow: hidden; }
  body {
    background: var(--backdrop);
    font-family: "Arimo", Arial, sans-serif;
    position: relative;
  }
  .card {
    position: absolute;
    width: 600px;
    height: 340px;
    background: var(--card-white);
    overflow: hidden;
    box-shadow: 0 12px 30px rgba(0,0,0,.45);
  }
  .card-front { left: 300px; top: 70px; }
  .card-back { left: 300px; top: 470px; }

  /* wordmark */
  .wordmark {
    color: var(--brand-blue);
    font-weight: 700;
    letter-spacing: .5px;
    line-height: 1.05;
    text-transform: uppercase;
  }
  .wordmark-mark {
    display: inline-block;
    width: 14px; height: 14px;
    background: var(--brand-blue);
    margin-right: 8px;
    vertical-align: middle;
  }

  /* front */
  .front-brand {
    position: absolute;
    left: 80px; top: 62px;
    font-size: 26px;
  }
  .front-tagline {
    position: absolute;
    left: 40px; top: 138px;
    width: 270px;
    font-size: 10.5px;
    color: var(--text-grey);
    line-height: 1.35;
  }
  .contact-block {
    position: absolute;
    left: 330px; top: 110px;
    width: 270px; height: 230px;
    background: var(--brand-blue);
    border-top: 6px solid var(--band-grey);
  }
  .name-band {
    position: absolute;
    left: 0; top: 230px;
    width: 330px; height: 110px;
    background: var(--brand-blue);
    border-top: 6px solid var(--band-grey);
  }
  .person {
    position: absolute;
    left: 34px; top: 14px;
    color: var(--text-white);
  }
  .person-name { font-size: 22px; font-weight: 700; }
  .person-role { font-size: 13px; margin-top: 2px; }
  .person-address {
    display: flex; gap: 8px;
    margin-top: 8px;
    font-size: 13px; line-height: 1.3;
  }
  .contact-list {
    position: absolute;
    left: 30px; top: 24px;
    list-style: none;
    color: var(--text-white);
    font-size: 13px;
  }
  .contact-list li {
    display: flex; align-items: center; gap: 9px;
    margin-bottom: 8px;
  }
  .icon { width: 13px; height: 13px; flex: none; fill: var(--text-white); }

  /* back */
  .back-brand {
    position: absolute;
    left: 40px; top: 120px;
    width: 270px;
    text-align: center;
    font-size: 30px;
  }
  .back-url {
    position: absolute;
    left: 40px; top: 250px;
    width: 270px;
    text-align: center;
    color: var(--brand-blue);
    font-weight: 700;
    font-size: 15px;
    letter-spacing: 5px;
  }
  .programs-panel {
    position: absolute;
    right: 0; top: 0;
    width: 250px; height: 100%;
    background: linear-gradient(135deg, var(--panel-grey-light), var(--panel-grey-dark));
  }
  .programs-rule {
    position: absolute;
    left: 10px; top: 48px;
    width: 6px; height: 216px;
    background: var(--brand-blue);
  }
  .programs {
    position: absolute;
    left: 30px; top: 44px;
    color: var(--text-white);
  }
  .programs-title { font-size: 16px; font-weight: 700; margin-bottom: 6px; }
  .programs-list { list-style: none; font-size: 13px; line-height: 1.3; }
  .programs-list li::before { content: "•"; margin: 0 9px 0 10px; }
</style>
</head>
<body>

<section class="card card-front" aria-label="Business card front">
  <div class="wordmark front-brand"><span class="wordmark-mark"></span>OakVRT Mortgage</div>
  <p class="front-tagline">We make the journey of buying a home or refinancing a mortgage easy. You can depend on us to help you find the perfect loan program for you.</p>

  <div class="contact-block">
    <ul class="contact-list">
      <li><svg class="icon" viewBox="0 0 16 16"><path d="M3.5 1l3 3-2 2c1 2 3.5 4.5 5.5 5.5l2-2 3 3-2 2.5C8 14.5 1.5 8 1 3.5z"/></svg>555 014 2080</li>
      <li><svg class="icon" viewBox="0 0 16 16"><path d="M4 1h8v4H4zM1 6h14v7h-3v2H4v-2H1zm4 5v3h6v-3z"/></svg>555 014 2081</li>
      <li><svg class="icon" viewBox="0 0 16 16"><path d="M1 3h14v10H1zm1.5 1.5L8 9l5.5-4.5v-.2H2.5z"/></svg>info@oakvrt.com</li>
      <li><svg class="icon" viewBox="0 0 16 16"><path d="M8 1a7 7 0 1 0 0 14A7 7 0 0 0 8 1zm-1 10V5l4.5 3z"/></svg>www.oakvrt.com</li>
    </ul>
  </div>

  <div class="name-band">
    <div class="person">
      <div class="person-name">Dana Whitfield</div>
      <div class="person-role">Manager</div>
      <div class="person-address">
        <svg class="icon" viewBox="0 0 12 16"><path d="M6 0a6 6 0 0 0-6 6c0 4.5 6 10 6 10s6-5.5 6-10a6 6 0 0 0-6-6zm0 8.5A2.5 2.5 0 1 1 6 3.5a2.5 2.5 0 0 1 0 5z"/></svg>
        <span>Unit 4B, 780 Maple Row<br>Fairview OR 97201 BAYSIDE</span>
      </div>
    </div>
  </div>
</section>

<section class="card card-back" aria-label="Business card back">
  <div class="wordmark back-brand"><span class="wordmark-mark"></span>OakVRT<br>Mortgage</div>
  <div class="back-url">www.oakvrt.com</div>

  <div class="programs-panel">
    <div class="programs-rule"></div>
    <div class="programs">
      <h2 class="programs-title">LOAN PROGRAMS</h2>
      <ul class="programs-list">
        <li>Jumbo Mortgages</li>
        <li>30 Year Fixed</li>
        <li>15 Year Fixed</li>
        <li>FHA Home Loan</li>
        <li>VA 30 Year Fixed</li>
        <li>HARP 2.0</li>
        <li>Reverse Mortgages</li>
        <li>FHA Home Loan</li>
        <li>VA 30 Year Fixed</li>
        <li>HARP 2.0</li>
        <li>Reverse Mortgages</li>
      </ul>
    </div>
  </div>
</section>

</body>
</html>
```